Lawn Company needs design work on a service call flyer!

We are a lawn care company that fertilizes and sprays lawns. This design is meant to be left behind at the customers house after a lawn application has been done too let them know what we have done.

The finished design will be printed on A6 paper (4.1 x 5.8 inches)

I have attached PDF files of the text that I want on the front of the document and the back of the document. I also included a sample design that I had been working on to give some idea what I would like. I don't want the same design, but you can use it as a building block for something new or come up with something entirely different.

FRONT: The front of the design is most important.

BACK: Other then the text the design should be minimal. If possible I would like an outline of the trees in my logo to be a backdrop. I have attached a PDF of the back of my business card as an example

The winning design will be a professional looking document that flows and reflects a lawn care business. Please contact me if you have any questions. I will only pick a design that is better then my current template.

Thank You

Target Market(s)

Lawn Care Customers

Industry/Entity Type

Lawn Care

Requirements
Must have
• 1. Our Logo
• 2. The attached text for the front & back of document
• 3. Our phone number (555-418-7390)
• 4. Our Email address (hollowfernturf@mailpost.example)
Nice to have
• A green theme with flowing graphics
Should not have
• any pictures of houses, people, or tools
• Don't copy the text or design from my design template. It is outdated, is it meant to be an example only

```html
<!DOCTYPE html>
<html lang="en">
<head>
<meta charset="utf-8">
<title>Hollow Fern Turf – Service Call Flyer</title>
<link href="https://fonts.googleapis.com/css2?family=Open+Sans:wght@400;600;700;800&display=swap" rel="stylesheet">
<style>
  :root{
    --bg:#d9d9d9;
    --paper:#ffffff;
    --mint:#e3f3dc;
    --green:#55b548;
    --green-dark:#2f8f2a;
    --ink:#3f3c3b;
    --ink-soft:#6a6664;
    --trunk:#4a4240;
    --leaf-red:#c9463f;
    --ghost:#dff0d8;
  }
  *{box-sizing:border-box;margin:0;padding:0}
  html,body{width:1200px;height:960px;overflow:hidden}
  body{background:var(--bg);font-family:"Open Sans",Arial,sans-serif;color:var(--ink);position:relative}

  .sheet{position:absolute;top:112px;width:520px;height:736px;background:var(--paper);overflow:hidden;box-shadow:0 6px 18px rgba(0,0,0,.18)}
  .sheet--front{left:60px}
  .sheet--back{left:620px}

  .grass-band{position:absolute;left:0;right:0;bottom:0;height:150px;
    background:linear-gradient(180deg,rgba(85,181,72,0) 0%,rgba(85,181,72,.35) 45%,var(--green) 100%)}

  /* FRONT */
  .front-tree{position:absolute;left:0;top:120px;width:250px;height:470px;
    background:linear-gradient(160deg,var(--leaf-red) 0%,#b86a62 30%,var(--trunk) 62%,#8fbf7f 100%);opacity:.9}
  .front-veil{position:absolute;left:120px;top:120px;right:0;height:450px;background:rgba(255,255,255,.72)}
  .front-top{position:absolute;left:0;right:0;top:0;height:120px;background:linear-gradient(180deg,#fff 0%,#f3faf0 100%)}
  .front-content{position:absolute;left:40px;right:34px;top:26px}
  .app-title{text-align:right;font-size:24px;font-weight:600;letter-spacing:1px;border-bottom:1px dotted var(--ink-soft);padding-bottom:4px}
  .field-row{display:flex;gap:10px;align-items:flex-end;font-size:11px;font-weight:600;margin-top:14px}
  .field-row .line{flex:1;border-bottom:1px dotted var(--ink-soft);height:12px}
  .serviced{text-align:right;font-size:12px;font-weight:600;line-height:1.45;margin-top:18px;text-transform:uppercase}
  .consists{font-size:21px;font-weight:700;margin-top:26px;text-align:right}
  .checklist{list-style:none;margin-top:10px;text-align:right;font-size:14px}
  .checklist li{display:flex;justify-content:flex-end;align-items:center;gap:10px;margin-top:7px}
  .checklist .box{width:14px;height:14px;border:1.5px solid var(--ink-soft);display:inline-block}
  .checklist .note{font-size:9px;font-style:italic;color:var(--ink-soft);margin-top:2px;text-align:right}
  .checklist .other-line{width:150px;border-bottom:1px dotted var(--ink-soft);height:12px}
  .watering{display:flex;align-items:flex-end;gap:8px;font-size:14px;font-weight:700;margin-top:26px}
  .watering .line{flex:1;border-bottom:1px dotted var(--ink-soft);height:12px}
  .promise{font-size:10.5px;font-style:italic;line-height:1.5;color:var(--ink);margin-top:34px;padding-bottom:12px;border-bottom:1.5px solid var(--ink)}
  .front-footer{position:absolute;left:40px;right:34px;top:624px;display:flex;justify-content:space-between;align-items:center;z-index:2}
  .brand{display:flex;align-items:center;gap:8px;font-size:17px;font-weight:800;color:var(--green-dark)}
  .brand-dot{width:14px;height:14px;border-radius:50%;background:var(--green-dark)}
  .contact{text-align:right;font-size:14px;font-weight:700;color:var(--green-dark);line-height:1.5}
  .contact .phone{font-size:17px}

  /* BACK */
  .back-wash{position:absolute;inset:0;background:linear-gradient(180deg,#fff 0%,#fff 45%,var(--mint) 80%)}
  .back-corner{position:absolute;top:0;left:0}
  .back-tree{position:absolute;right:14px;top:10px;width:196px;height:118px;border-radius:6px;
    background:linear-gradient(135deg,#3f7f38 0%,var(--trunk) 55%,#4ea545 100%);opacity:.55}
  .side-title{position:absolute;left:0;top:0;width:640px;height:28px;transform-origin:0 0;transform:translate(24px,720px) rotate(-90deg);
    font-size:19px;font-weight:700;letter-spacing:1.5px;white-space:nowrap;color:var(--ink)}
  .back-content{position:absolute;left:70px;right:30px;top:40px}
  .section-title{font-size:18px;font-weight:800;color:var(--green-dark);line-height:1.1;text-transform:uppercase}
  .intro{font-size:11px;font-weight:700;line-height:1.4;margin-top:8px;max-width:200px}
  .intro--wide{max-width:none}
  .tips{list-style:none;margin-top:10px}
  .tips li{position:relative;padding-left:12px;font-size:10px;line-height:1.45;margin-top:6px;color:var(--ink-soft)}
  .tips li::before{content:"";position:absolute;left:0;top:5px;width:6px;height:6px;border-radius:50%;background:var(--green)}
  .mowing{margin-top:34px}
  .ghost-name{position:absolute;left:70px;bottom:40px;font-size:36px;font-weight:800;color:var(--ghost);letter-spacing:2px;line-height:1}
</style>
</head>
<body>

<section class="sheet sheet--front" aria-label="Front of flyer">
  <div class="front-top"></div>
  <div class="front-tree" role="img" aria-label="Illustrated tree with dark trunk and red leaves"></div>
  <div class="front-veil"></div>
  <div class="grass-band" role="img" aria-label="Green grass blades along the bottom edge"></div>

  <div class="front-content">
    <h1 class="app-title">APPLICATION</h1>
    <div class="field-row"><span>TIME</span><span class="line"></span><span>DATE</span><span class="line"></span></div>
    <p class="serviced">Your lawn has been<br>professionally serviced today</p>
    <div class="field-row"><span>BY</span><span class="line"></span></div>
    <h2 class="consists">Today's application consists of</h2>
    <ul class="checklist">
      <li>Seasonally Balanced Slow Release Fertilizer <span class="box"></span></li>
      <li>Broadleaf Weed Control <span class="box"></span></li>
      <li class="note">(Please keep off the lawn until it is thoroughly dry)</li>
      <li>Other <span class="other-line"></span></li>
    </ul>
    <p class="watering"><span>Please begin watering the lawn</span><span class="line"></span><span>after application</span></p>
    <p class="promise">"We strive to complete work in a professional manner each and every visit. If you are not satisfied with the level of service you are receiving please contact us. We value your business and wish to maintain long-term relationships with our customers."</p>
  </div>

  <div class="front-footer">
    <div class="brand"><span class="brand-dot"></span>Hollow Fern Turf</div>
    <div class="contact">
      <div class="phone">555-418-7390</div>
      <div>hollowfernturf@mailpost.example</div>
    </div>
  </div>
</section>

<section class="sheet sheet--back" aria-label="Back of flyer">
  <div class="back-wash"></div>
  <svg class="back-corner" width="520" height="240" viewBox="0 0 520 240" aria-hidden="true">
    <polygon points="170,0 520,0 520,145" fill="var(--green)"/>
  </svg>
  <div class="back-tree" role="img" aria-label="Outline of trees as a backdrop in the top corner"></div>
  <div class="grass-band" role="img" aria-label="Green grass blades along the bottom edge"></div>
  <div class="ghost-name">HOLLOW FERN TURF</div>

  <p class="side-title">For best results please follow these general Guidelines</p>

  <div class="back-content">
    <h2 class="section-title">Watering<br>your lawn</h2>
    <p class="intro">When rainfall is not sufficient to meet your lawns watering needs, follow these guidelines for a lush green lawn</p>
    <ul class="tips">
      <li>Your lawn requires approx 1 - 1.5 inches of water per week, sometimes more in hot, dry weather.</li>
      <li>Avoid short frequent watering. It is best to water deeply once every 5 - 7 days. This encourages deep root growth.</li>
      <li>You can use a Frisbee or an empty tuna can to measure the amount you have watered. Just place it in the path of the sprinkler and when it is full, move your sprinkler to a new location.</li>
      <li>Aerating your lawn once a year will help your lawn utilize more water and prevent unnecessary runoff.</li>
    </ul>

    <div class="mowing">
      <h2 class="section-title">Mowing<br>your lawn</h2>
      <p class="intro intro--wide">Mowing your lawn properly can make all the difference in how it looks throughout the year</p>
      <ul class="tips">
        <li>You should mow your lawn at 2.5 - 3 inches (no shorter). Mowing at this length helps shade your roots and provides more leaf surface for your lawn to manufacture its own food. As an added bonus it will help your lawn retain its moisture and reduce watering requirements.</li>
        <li>As a general rule, try not to remove more then 1/3 of the leave blade in a single mowing. During periods of heavy growth, this may mean mowing more frequently then usual.</li>
        <li>Always ensure your lawn mower is maintained and the blade is sharp so that is cuts cleanly.</li>
        <li>Your last mowing in the fall should be shorter, about 2 inches.</li>
      </ul>
    </div>
  </div>
</section>

</body>
</html>
```